Corveth Thermal Job Add

We need a flashy ad we can post around our marketplace to attract new talent and employee. Our website has our company theme https://corveththermal.ca/

Target Market(s)

HVAC, Refrigeration, Trades

Industry/Entity Type

Trades

Requirements
Must have
• a few key phrases such as "Paying above industry standard" and "No on-call requirements"

```html
<!DOCTYPE html>
<html lang="en">
<head>
<meta charset="utf-8">
<title>Corveth Thermal – We Are Hiring</title>
<link rel="stylesheet" href="https://fonts.googleapis.com/css2?family=Anton&family=Bebas+Neue&family=Lato:wght@700;900&display=swap">
<style>
  :root {
    --page-bg: #e4e4e4;
    --white: #ffffff;
    --brand-blue: #1a8cf5;
    --brand-blue-deep: #0870c9;
    --brand-orange: #f05c25;
    --ink: #0b0b0b;
  }
  html, body {
    margin: 0;
    padding: 0;
    width: 1200px;
    height: 1200px;
    overflow: hidden;
    background: var(--page-bg);
  }
  .flyer {
    position: absolute;
    left: 151px;
    top: 20px;
    width: 898px;
    height: 1160px;
    overflow: hidden;
    background: var(--white);
  }
  .flyer-art { display: block; width: 100%; height: 100%; }
  .brand-name {
    font-family: 'Anton', sans-serif;
    fill: var(--brand-blue-deep);
    letter-spacing: 2px;
  }
  .headline {
    font-family: 'Anton', sans-serif;
    fill: var(--brand-blue);
  }
  .perks {
    font-family: 'Bebas Neue', sans-serif;
    fill: var(--white);
  }
  .website {
    font-family: 'Lato', sans-serif;
    font-weight: 900;
    fill: var(--brand-orange);
  }
  .phone-number {
    font-family: 'Lato', sans-serif;
    font-weight: 900;
    fill: var(--white);
  }
</style>
</head>
<body>
  <div class="flyer">
    <svg class="flyer-art" viewBox="0 0 1355 1750" xmlns="http://www.w3.org/2000/svg">
      <!-- header -->
      <rect class="header-bg" x="0" y="0" width="1355" height="1750" fill="var(--white)"/>
      <circle class="brand-dot" cx="255" cy="140" r="70" fill="var(--brand-orange)"/>
      <text class="brand-name" x="355" y="190" font-size="120" textLength="900" lengthAdjust="spacingAndGlyphs">CORVETH THERMAL INC</text>

      <!-- orange wave band and blue field -->
      <path class="wave-orange" d="M0 298 C 300 255, 700 250, 1000 292 C 1180 300, 1300 230, 1355 105 L1355 1750 L0 1750 Z" fill="var(--brand-orange)"/>
      <path class="field-blue" d="M0 365 C 300 275, 650 262, 1000 297 C 1120 305, 1260 250, 1355 170 L1355 1750 L0 1750 Z" fill="var(--brand-blue)"/>

      <!-- dark block behind headline -->
      <polygon class="shadow-block" fill="var(--ink)" points="0,485 136,349 722,349 722,690 830,690 830,1090 1355,1090 1355,1431 1081,1750 0,1750"/>

      <!-- corner accent -->
      <polygon class="corner-accent" fill="var(--brand-orange)" points="1355,1491 1355,1750 1131,1750"/>

      <!-- headline -->
      <text class="headline" x="136" y="673" font-size="380" textLength="574" lengthAdjust="spacingAndGlyphs">WE</text>
      <text class="headline" x="129" y="1049" font-size="380" textLength="688" lengthAdjust="spacingAndGlyphs">ARE</text>
      <text class="headline" x="154" y="1431" font-size="380" textLength="1195" lengthAdjust="spacingAndGlyphs">HIRING</text>

      <!-- perks -->
      <text class="perks" x="163" y="1532" font-size="58" textLength="1030" lengthAdjust="spacingAndGlyphs">PAYING ABOVE INDUSTRY STANDARD  |  NO ON-CALL REQUIREMENTS</text>

      <!-- website -->
      <g class="globe-icon" fill="none" stroke="var(--brand-orange)" stroke-width="3.5">
        <circle cx="176" cy="1583" r="14"/>
        <ellipse cx="176" cy="1583" rx="6" ry="14"/>
        <line x1="162" y1="1583" x2="190" y2="1583"/>
      </g>
      <rect x="203" y="1567" width="3" height="32" fill="var(--brand-orange)"/>
      <text class="website" x="224" y="1598" font-size="46" textLength="640" lengthAdjust="spacingAndGlyphs">www.corveththermal.ca</text>

      <!-- phone pill -->
      <g class="phone-pill">
        <clipPath id="pill-clip"><rect x="138" y="1621" width="903" height="90" rx="45"/></clipPath>
        <g clip-path="url(#pill-clip)">
          <rect x="138" y="1621" width="460" height="90" fill="var(--brand-blue)"/>
          <rect x="598" y="1621" width="443" height="90" fill="var(--brand-orange)"/>
        </g>
        <rect x="138" y="1621" width="903" height="90" rx="45" fill="none" stroke="var(--white)" stroke-width="4"/>
        <text class="phone-number" x="175" y="1684" font-size="52" textLength="370" lengthAdjust="spacingAndGlyphs">(403) 555-0182</text>
        <circle cx="598" cy="1666" r="32" fill="var(--ink)"/>
        <path class="phone-icon" fill="var(--white)" d="M585 1650 l8 -3 l6 12 l-5 4 c2 6 6 10 12 12 l4 -5 l12 6 l-3 8 c-2 3 -6 4 -10 3 c-14 -4 -24 -14 -28 -28 c-1 -4 0 -7 4 -9 z"/>
        <text class="phone-number" x="648" y="1684" font-size="52" textLength="370" lengthAdjust="spacingAndGlyphs">(780) 555-0147</text>
      </g>
    </svg>
  </div>
</body>
</html>
```